Reset your nervous system - Reelnest VOD Poster

Glow7Care helps people clear emotional issues and positively improve their behaviours and thoughts as a result. We use a combination of energy psychology, energy medicine, kinesiology and coaching to achieve results in a brief period of time compared to conventional therapies. See http://www.glow7care.example

I'm selling a video on Reelnest's Video on Demand service and they required a poster for my product for the product landing page. You can see the poster for my previous product on the page https://reelnest.example/ondemand/shedpoundswithpulsework - the poster is down in the right-hand side column and has the women holding the cake and the apple. This was a previous Forty Studios winner.

Let me tell you about the new video product and then I'll give you the specs for the poster image.

My new product is a video of a workshop in which I presented three Energy Techniques that relieve stress and anxiety by working directly with the brain and nervous system. It was a one hour workshop presented to a live audience accompanied with slides. You can see the trailer on reelnest: http://qlnk.example/3-methods

So the techniques presented in the video can help people with stress, anxiety, panic attacks, emotional eating, addictions, PTSD, trauma and abuse in a very gentle way.

I'd like the colours on the poster to be taken from my website (http://www.glow7care.example) and the previous designs done for me (see my profile).

According to reelnest, the poster should be a JPG or PNG and 1080px by 1600px.

You can play with the wording on the poster. Variations could include:
+ Reset Flight / Fight /Freeze
+ Reset Your Nervous System with 3 powerful techniques
+ Reset Stress, Anxiety and Panic with these 3 Powerful Techniques
+ Reset Your Nervous System
+ Relax Your Nervous System
+ 3 Techniques to Reset Stress, Anxiety, Panic, and Trauma
+ ??
You get the idea from the trailer video above.

```html
<!DOCTYPE html>
<html lang="en">
<head>
<meta charset="utf-8">
<title>Reset Your Nervous System – Glow7Care Poster</title>
<link rel="stylesheet" href="https://fonts.googleapis.com/css2?family=Montserrat:wght@800&family=Roboto+Slab:wght@600&display=swap">
<style>
  :root {
    --brown: #834a0a;
    --brown-line: #7a4309;
    --dark: #3a2008;
    --tan: #c89a62;
    --white: #ffffff;
    --photo-light: #eef2f6;
    --photo-mid: #b9cde0;
  }
  html, body {
    margin: 0;
    padding: 0;
    overflow: hidden;
  }
  .poster {
    position: relative;
    width: 810px;
    height: 1200px;
    overflow: hidden;
    background: var(--brown);
    font-family: "Montserrat", Arial, sans-serif;
    font-weight: 800;
    color: var(--white);
  }
  .photo-area {
    position: absolute;
    left: 0;
    top: 607px;
    width: 810px;
    height: 398px;
    background: radial-gradient(ellipse at 50% 60%, var(--photo-mid) 0%, #d7e3ee 45%, var(--photo-light) 100%);
  }
  .footer-band {
    position: absolute;
    left: 0;
    top: 1005px;
    width: 810px;
    height: 195px;
    background: var(--dark);
  }
  .frame {
    position: absolute;
    inset: 0;
    pointer-events: none;
  }
  .tag {
    position: absolute;
    left: 60px;
    width: 133px;
    height: 43px;
    border: 2px solid var(--white);
    background: var(--brown);
    font-size: 27px;
    line-height: 43px;
    text-align: center;
    letter-spacing: 0.5px;
  }
  .tag::before {
    content: "";
    position: absolute;
    left: -9px;
    top: 13px;
    border-top: 8px solid transparent;
    border-bottom: 8px solid transparent;
    border-left: 7px solid var(--white);
  }
  .tag::after {
    content: "";
    position: absolute;
    left: -2px;
    top: 45px;
    width: 106px;
    height: 14px;
    background: rgba(58, 32, 8, 0.55);
    clip-path: polygon(0 0, 100% 0, 100% 100%, 0 30%);
  }
  .headline {
    position: absolute;
    left: 208px;
    margin: 0;
    font-size: 27.5px;
    line-height: 29.5px;
    text-transform: uppercase;
    white-space: nowrap;
  }
  .summary {
    position: absolute;
    left: 64px;
    top: 515px;
    margin: 0;
    font-size: 29px;
    line-height: 32px;
    text-transform: uppercase;
  }
  .summary::before {
    content: "";
    position: absolute;
    left: -20px;
    top: 14px;
    border-top: 8px solid transparent;
    border-bottom: 8px solid transparent;
    border-left: 7px solid var(--white);
  }
  .summary .accent { color: var(--tan); }
  .brand {
    position: absolute;
    left: 44px;
    top: 1050px;
    margin: 0;
    font-size: 58px;
    line-height: 1;
    color: var(--white);
  }
  .web-plaque {
    position: absolute;
    left: 510px;
    top: 1080px;
    width: 300px;
    height: 45px;
    background: var(--tan);
    clip-path: polygon(0 0, 100% 0, 100% 100%, 9% 100%);
    font-family: "Roboto Slab", Georgia, serif;
    font-weight: 600;
    font-size: 18px;
    line-height: 45px;
    color: var(--dark);
    text-align: center;
    padding-left: 20px;
    box-sizing: border-box;
  }
</style>
</head>
<body>
<main class="poster">
  <div class="photo-area" role="img" aria-label="Photo of a worried middle-aged couple sitting together, holding their heads in stress"></div>
  <div class="footer-band"></div>

  <svg class="frame" width="810" height="1200" viewBox="0 0 810 1200" aria-hidden="true">
    <path d="M585,0 L810,0 L810,245 C790,120 710,30 585,0 Z" fill="var(--dark)"/>
    <path d="M560,0 C690,20 790,110 810,230" fill="none" stroke="var(--white)" stroke-width="5"/>
    <path d="M43,607 L43,41 L560,41 C690,41 767,150 767,300 L767,607" fill="none" stroke="var(--white)" stroke-width="2.5"/>
    <path d="M767,607 L767,965 L140,965 C80,965 43,900 43,800 L43,607" fill="none" stroke="var(--brown-line)" stroke-width="2.5"/>
    <path d="M0,870 C20,960 80,1005 160,1005 L0,1005 Z" fill="var(--dark)"/>
    <path d="M500,1080 L525,1080 L550,1125 L525,1125 Z" fill="none" stroke="var(--tan)" stroke-width="1"/>
  </svg>

  <div class="tag" style="top:60px">Reset</div>
  <h1 class="headline" style="top:79px">Flight / Fight /Freeze</h1>

  <div class="tag" style="top:148px">Reset</div>
  <p class="headline" style="top:145px">Your nervous system with<br>3 powerful techniques</p>

  <div class="tag" style="top:237px">Reset</div>
  <p class="headline" style="top:233px">Stress, anxiety and panic<br>with these 3 powerful<br>techniques</p>

  <div class="tag" style="top:343px">Reset</div>
  <p class="headline" style="top:359px">Your nervous system</p>

  <div class="tag" style="top:432px">Relax</div>
  <p class="headline" style="top:453px">Your nervous system</p>

  <p class="summary"><span class="accent">3 Techniques to reset stress</span>,<br>anxiety, panic, and trauma</p>

  <p class="brand">Glow7Care</p>
  <div class="web-plaque">www.glow7care.example</div>
</main>
</body>
</html>
```